Branded Powerpoint Slide update

Design a clean, modern, professional corporate powerpoint template that include the Brightwell Corporation word-mark logo, brand color, and brand font. The design should come with a variety of sample pages - I have attached a Template sample of what the template should include. I have also included a sample slide that contains newly created brand elements. Feel free to use this as a guide.
Templates should be produced in A4 and Letter formats as a powerpoint file and should use Helvetica Now Display as the embedded font.
Design Preferences:
Cover should stand alone with engaging elements. Overall, design elements should remain minimal as to not dominate the slide. Colour block designs, solid borders with flowing smooth lines, single side borders with connected header and footer, cut off or half page headers and footers are all acceptable.
Enclosed are:
1. Three word mark logos with reverse versions of each, one for each primary brand colour. ('b-invert, o-invert, 0-main, b-main)
2. Brightwell corporate colour pallet (brightwell brand... )
3. Helvetica Now Display font files
4. Sample of Powerpoint template to show types of pages needed for inclusion ('Sample Slide Deck.ppt)
5. Sample of newly created brand elements for simple Header/Text Body slide. (both 'letterhead...ai" files are the raw files. 'Powerpoint slide Template Sample' is the sample being used).
Technology Equipment

```html
<!DOCTYPE html>
<html lang="en">
<head>
<meta charset="utf-8">
<title>Brightwell Presentation Template</title>
<link href="https://fonts.googleapis.com/css2?family=Inter:ital,wght@0,400;0,500;0,600;0,700;0,800;1,400&display=swap" rel="stylesheet">
<style>
:root{
  --brand-blue:#1ba6f6;
  --brand-blue-deep:#0e8fe0;
  --brand-red:#ff3b12;
  --ink:#1f1f1f;
  --body:#555;
  --page-bg:#efefef;
  --white:#fff;
}
*{margin:0;padding:0;box-sizing:border-box}
html,body{width:1200px;height:4310px;overflow:hidden;background:var(--page-bg);font-family:"Inter",Arial,sans-serif;color:var(--ink)}
.slide{position:absolute;left:43px;width:1107px;height:623px;background:var(--white);overflow:hidden}
.abs{position:absolute}
.photo-blue{position:absolute;inset:0;background:linear-gradient(160deg,#2ab0fb 0%,#1aa3f3 55%,#139ae9 100%)}
.wordmark{font-weight:800;letter-spacing:-0.02em;line-height:1}
.footer-band{position:absolute;left:0;bottom:0;width:100%;height:43px;background:var(--brand-blue)}
.footer-page{position:absolute;left:0;top:0;width:124px;height:43px;background:var(--brand-red);color:var(--white);font-size:17px;font-weight:500;padding:12px 0 0 33px}
.footer-copy{position:absolute;right:38px;top:14px;color:var(--white);font-size:13px}
.slide-heading{position:absolute;left:23px;top:22px;font-size:31px;font-weight:500;letter-spacing:-0.01em}
.slide-sub{position:absolute;left:25px;top:68px;font-size:15px;color:#333}
/* cover */
.cover-logo{left:0;width:100%;top:150px;text-align:center;color:var(--white);font-size:112px}
.cover-title{left:0;width:100%;top:286px;text-align:center;color:var(--white);font-size:43px;font-weight:600;letter-spacing:-0.01em}
.cover-text{left:160px;width:787px;top:348px;text-align:center;color:var(--white);font-size:13.5px;line-height:26px}
.cover-arrow{left:535px;top:449px}
/* bullets */
.bullet-list{position:absolute;left:20px;top:140px;list-style:none;width:470px}
.bullet-list li{position:relative;padding-left:30px;font-size:14.3px;line-height:24px;margin-bottom:12px;color:#222}
.bullet-list li::before{content:"";position:absolute;left:1px;top:5px;width:14px;height:14px;border:2px solid var(--brand-blue);border-radius:50%}
.bullet-list li::after{content:"";position:absolute;left:6px;top:10px;width:8px;height:8px;background:var(--brand-blue);border-radius:50%}
/* team */
.member{position:absolute;top:139px;width:250px;text-align:center}
.member-photo{width:164px;height:164px;border-radius:50%;margin:0 auto;background:radial-gradient(circle at 50% 40%,#d8d8d8,#9a9a9a)}
.member-name{color:var(--brand-blue);font-size:16.5px;font-weight:600;margin-top:18px}
.member-role{font-size:11.5px;margin-top:6px;color:#333}
.member-bio{font-size:13px;line-height:24px;color:#444;margin-top:12px}
.social{display:flex;justify-content:center;gap:14px;margin-top:14px}
.social span{width:36px;height:36px;border-radius:50%;background:var(--brand-red)}
/* quote */
.quote-mark{left:0;width:100%;top:190px;text-align:center;color:var(--white);font-size:150px;font-weight:800;line-height:1;font-family:Georgia,serif}
.quote-text{left:105px;width:897px;top:300px;text-align:center;color:var(--white);font-size:25px;font-style:italic;line-height:39px}
/* cards */
.card{position:absolute;top:120px;width:340px;height:417px;background:var(--white);box-shadow:0 0 8px rgba(0,0,0,.14);text-align:center;padding:0 22px}
.card-icon{width:80px;height:80px;margin:42px auto 0;border:3px solid var(--brand-blue);border-radius:10px;background:#e6f5fe}
.card-title{color:var(--brand-blue);font-size:22px;font-weight:500;margin-top:32px}
.card-text{font-size:12.6px;line-height:24px;color:#444;margin-top:12px}
/* thank you */
.thanks-top{position:absolute;left:0;top:0;width:100%;height:410px}
.thanks-rule{position:absolute;left:0;top:410px;width:100%;height:4px;background:var(--brand-red)}
.thanks-logo{left:0;width:100%;top:110px;text-align:center;color:var(--white);font-size:118px}
.thanks-title{left:0;width:100%;top:262px;text-align:center;color:var(--white);font-size:44px;font-weight:500}
.contact{position:absolute;top:385px;width:300px;text-align:center;font-size:16px;line-height:23px;color:#333}
.contact-icon{width:60px;height:60px;margin:0 auto 16px;background:var(--white);box-shadow:0 2px 6px rgba(0,0,0,.15);display:flex;align-items:center;justify-content:center}
</style>
</head>
<body>

<!-- Cover -->
<section class="slide" style="top:50px">
  <div class="photo-blue" role="img" aria-label="City skyline photograph under a blue tint"></div>
  <div class="abs wordmark cover-logo">Brightwell</div>
  <h1 class="abs cover-title">THIS IS YOUR PRESENTATION TITLE</h1>
  <p class="abs cover-text">Lorem ipsum dolor sit amet, consectetur adipiscing elit, sed do eiusmod tempor incididunt ut labore et dolore magna aliqua. Quis ips suspendisse ultrices gravida. Risus commodo viverra maecenas accumsan lacus vel facilisis. Lorem ipsum dolor sit amet, consectetur adipiscing elit, sed do eiusmod</p>
  <svg class="abs cover-arrow" width="36" height="36" viewBox="0 0 36 36"><circle cx="18" cy="18" r="16" fill="none" stroke="#fff" stroke-width="1.6"/><path d="M18 9v17M11 19l7 7 7-7" fill="none" stroke="#fff" stroke-width="1.6"/></svg>
</section>

<!-- Page 2 -->
<section class="slide" style="top:765px">
  <h2 class="slide-heading">Heading Text Goes Here</h2>
  <p class="slide-sub">Lorem ipsum dolor sit amet, consectetur adipiscing elit, sed do</p>
  <ul class="bullet-list">
    <li>Sed ut perspiciatis unde omnis iste natus error sit voluptatem accusantium doloremque laudantium, totam</li>
    <li>Sed ut perspiciatis unde omnis iste natus error sit voluptatem accusantium doloremque laudantium, totam</li>
    <li>Sed ut perspiciatis unde omnis iste natus error sit voluptatem accusantium doloremque laudantium, totam</li>
    <li>Sed ut perspiciatis unde omnis iste natus error sit voluptatem accusantium doloremque laudantium, totam</li>
    <li>Sed ut perspiciatis unde omnis iste natus error sit voluptatem accusantium doloremque laudantium, totam</li>
    <li>Sed ut perspiciatis unde omnis iste natus error sit voluptatem accusantium doloremque laudantium, totam</li>
  </ul>
  <svg class="abs" style="left:0;top:0" width="1107" height="580" viewBox="0 0 1107 580">
    <defs><linearGradient id="projector" x1="0" y1="0" x2="1" y2="1"><stop offset="0" stop-color="#7a0f16"/><stop offset=".5" stop-color="#3a0608"/><stop offset="1" stop-color="#120203"/></linearGradient></defs>
    <polygon points="598,0 1107,0 1107,580 489,580" fill="url(#projector)" role="img" aria-label="Photograph of a projector lens in red light"/>
    <line x1="598" y1="0" x2="489" y2="580" stroke="var(--brand-red)" stroke-width="6"/>
  </svg>
  <div class="abs wordmark" style="right:28px;top:16px;color:#fff;font-size:32px">Brightwell</div>
  <div class="footer-band"><div class="footer-page">Page 2</div><div class="footer-copy">© 2021 Brightwell. All Rights Reserved.</div></div>
</section>

<!-- Page 3 -->
<section class="slide" style="top:1480px">
  <h2 class="slide-heading">Our Team</h2>
  <p class="slide-sub">Lorem ipsum dolor sit amet, consectetur adipiscing elit, sed do</p>
  <div class="abs wordmark" style="right:28px;top:26px;color:var(--brand-blue);font-size:30px">Brightwell</div>
  <div class="member" style="left:-1px"><div class="member-photo" role="img" aria-label="Team member portrait"></div><div class="member-name">JOHN SMITH</div><div class="member-role">Sed ut per</div><p class="member-bio">Lorem ipsum dt, consecter adipiscing elit,ed do oempor incididunt ut labore et dolore Lore ipsum dt, consecLorem ipsum dt, consecter adipiscing</p><div class="social"><span></span><span></span><span></span><span></span></div></div>
  <div class="member" style="left:275px"><div class="member-photo" role="img" aria-label="Team member portrait"></div><div class="member-name">JOHN SMITH</div><div class="member-role">Sed ut per</div><p class="member-bio">Lorem ipsum dt, consecter adipiscing elit,ed do oempor incididunt ut labore et dolore Lore ipsum dt, consecLorem ipsum dt, consecter adipiscing</p><div class="social"><span></span><span></span><span></span><span></span></div></div>
  <div class="member" style="left:550px"><div class="member-photo" role="img" aria-label="Team member portrait"></div><div class="member-name">JOHN SMITH</div><div class="member-role">Sed ut per</div><p class="member-bio">Lorem ipsum dt, consecter adipiscing elit,ed do oempor incididunt ut labore et dolore Lore ipsum dt, consecLorem ipsum dt, consecter adipiscing</p><div class="social"><span></span><span></span><span></span><span></span></div></div>
  <div class="member" style="left:826px"><div class="member-photo" role="img" aria-label="Team member portrait"></div><div class="member-name">JOHN SMITH</div><div class="member-role">Sed ut per</div><p class="member-bio">Lorem ipsum dt, consecter adipiscing elit,ed do oempor incididunt ut labore et dolore Lore ipsum dt, consecLorem ipsum dt, consecter adipiscing</p><div class="social"><span></span><span></span><span></span><span></span></div></div>
  <div class="footer-band"><div class="footer-page">Page 3</div><div class="footer-copy">© 2021 Brightwell. All Rights Reserved.</div></div>
</section>

<!-- Quote -->
<section class="slide" style="top:2196px">
  <div class="photo-blue" role="img" aria-label="Office desk photograph under a blue tint"></div>
  <div class="abs quote-mark">“</div>
  <p class="abs quote-text">Lorem ipsum dolor sit amet, consectetur adipiscing elit, sed do eiusmod tempor incididunt ut labore et dolore magna aliqua. Quis ips suspendisse ultrices gravida. Risus commodo viverra maecenas accumsan lacus vel facilisis. Lorem ipsum dolor sit amet, consectetur adipiscing elit, sed do eiusmod</p>
</section>

<!-- Page 5 -->
<section class="slide" style="top:2911px">
  <h2 class="slide-heading">Heading Text Goes Here</h2>
  <p class="slide-sub">Lorem ipsum dolor sit amet, consectetur adipiscing elit, sed do</p>
  <div class="abs wordmark" style="right:25px;top:22px;color:var(--brand-blue);font-size:40px">Brightwell</div>
  <div class="card" style="left:25px"><div class="card-icon" role="img" aria-label="Documents icon"></div><h3 class="card-title">The standard Lorem</h3><p class="card-text">Lorem ip dolor sit amet, consectetur adipiscing elit, sed do eiusmod tempor incididunt ut labore et dolore mag aliqua. Quis ipsum suspendisse ultrices gravida. Ri commodo viverra maecenas accumsan lacus vel facilisis. Lorem ip dolor sit amet, consectetur adiscing elit, sed do eiusmod tempor incididunt ut lare et dolore mag aliqua. Quis ipsum suspendisse ultrices gravida</p></div>
  <div class="card" style="left:383px"><div class="card-icon" role="img" aria-label="Finance icon"></div><h3 class="card-title">The standard Lorem</h3><p class="card-text">Lorem ip dolor sit amet, consectetur adipiscing elit, sed do eiusmod tempor incididunt ut labore et dolore mag aliqua. Quis ipsum suspendisse ultrices gravida. Ri commodo viverra maecenas accumsan lacus vel facilisis. Lorem ip dolor sit amet, consectetur adiscing elit, sed do eiusmod tempor incididunt ut lare et dolore mag aliqua. Quis ipsum suspendisse ultrices gravida</p></div>
  <div class="card" style="left:741px"><div class="card-icon" role="img" aria-label="Team icon"></div><h3 class="card-title">The standard Lorem</h3><p class="card-text">Lorem ip dolor sit amet, consectetur adipiscing elit, sed do eiusmod tempor incididunt ut labore et dolore mag aliqua. Quis ipsum suspendisse ultrices gravida. Ri commodo viverra maecenas accumsan lacus vel facilisis. Lorem ip dolor sit amet, consectetur adiscing elit, sed do eiusmod tempor incididunt ut lare et dolore mag aliqua. Quis ipsum suspendisse ultrices gravida</p></div>
  <div class="footer-band"><div class="footer-page">Page 5</div><div class="footer-copy" style="right:25px">© 2021 Brightwell. All Rights Reserved.</div></div>
</section>

<!-- Thank you -->
<section class="slide" style="top:3627px">
  <div class="thanks-top"><div class="photo-blue" role="img" aria-label="Projector photograph under a blue tint"></div></div>
  <div class="thanks-rule"></div>
  <div class="abs wordmark thanks-logo">Brightwell</div>
  <div class="abs thanks-title">THANK YOU</div>
  <div class="contact" style="left:74px">
    <div class="contact-icon"><svg width="24" height="24" viewBox="0 0 24 24"><path d="M12 2a7 7 0 0 0-7 7c0 5 7 13 7 13s7-8 7-13a7 7 0 0 0-7-7z" fill="var(--brand-blue)"/><circle cx="12" cy="9" r="2.6" fill="#fff"/></svg></div>
    123 Avenue name, City name<br>10150, United States
  </div>
  <div class="contact" style="left:411px">
    <div class="contact-icon"><svg width="24" height="24" viewBox="0 0 24 24"><path d="M6.6 10.8a15 15 0 0 0 6.6 6.6l2.2-2.2a1 1 0 0 1 1-.25 11.4 11.4 0 0 0 3.6.57 1 1 0 0 1 1 1V20a1 1 0 0 1-1 1A17 17 0 0 1 3 4a1 1 0 0 1 1-1h3.5a1 1 0 0 1 1 1c0 1.25.2 2.45.57 3.6a1 1 0 0 1-.25 1z" fill="none" stroke="var(--brand-blue)" stroke-width="1.6"/></svg></div>
    Phone:<br>(888) 888-8888
  </div>
  <div class="contact" style="left:739px">
    <div class="contact-icon"><svg width="26" height="20" viewBox="0 0 26 20"><rect x="1" y="1" width="24" height="18" fill="var(--brand-blue)"/><path d="M1 1l12 10L25 1" fill="none" stroke="#fff" stroke-width="1.6"/></svg></div>
    Email:<br>info@brightwell.com
  </div>
</section>

</body>
</html>
```